Postcard double sided

Title: DWIGHT'S REVENGE

Why would Dwight Kessler align himself with Gordon Pruett?

(photo of two guys)

Dwight approached elected officials that he wanted to run for office, but did not have money to finance his campaign. He wanted other elected officials to finance his campaign. Everyone told him that they would help him get the vote out, but that he needed to finance his own race.

In comes Gordon Pruett.

Gordon Pruett who has a pay to play scheme over at the City, told Dwight he would finance his campaign on one condition.

He needed to run against Steven Hulse.

Why would Dwight want to run with no money?

Backside

DWIGHT'S REVENGE

Dwight decided to run because no one on the school board would terminate Dwight's ex and her new boyfriend who both work for the school district. His ex even filed criminal charges against him that are still pending.

Mug Shot facing left (name the charges Criminal Trespass , and Criminal Mischief (highlight bold letters use two lines) mug shot facing right

Complaint one (then photo with full face) Compliant 2)
(showcharges)

Dwight's ultimate goal is to terminate his ex and her new boyfriend if elected.
Plus Gordon Pruett needs the majority on the school board to do what he does bet.

Kickbacks for Contracts.

They will hire their own contractors!
Say "No" to Dwight's Revenge and Gordon Pruett Money Grab!

Title On Back: all caps: DOMESTIC VIOLENCE

```html
<!DOCTYPE html>
<html lang="en">
<head>
<meta charset="utf-8">
<title>Dwight's Revenge – Postcard</title>
<link href="https://fonts.googleapis.com/css2?family=Questrial&family=Poppins:wght@600;700&display=swap" rel="stylesheet">
<style>
  :root {
    --page-bg: #1b1b1b;
    --navy-deep: #03223a;
    --navy-mid: #0b4466;
    --navy-glow: #135d88;
    --ink: #0d2740;
    --ink-soft: #2b3b4c;
    --teal: #19f0d8;
    --white: #ffffff;
    --band: #021a2b;
    --paper: #fafafa;
    --rule: #9aa5ae;
  }
  * { box-sizing: border-box; margin: 0; padding: 0; }
  html, body { width: 848px; height: 1200px; overflow: hidden; }
  body {
    background: var(--page-bg);
    position: relative;
    font-family: "Questrial", sans-serif;
    color: var(--white);
  }
  .card {
    position: absolute;
    left: 27px;
    width: 791px;
    overflow: hidden;
    background: radial-gradient(ellipse at 45% 45%, var(--navy-glow) 0%, var(--navy-mid) 35%, var(--navy-deep) 80%);
  }
  .card--front { top: 30px; height: 553px; }
  .card--back { top: 612px; height: 554px; }
  .card .wave { position: absolute; left: 0; top: 0; width: 100%; height: 100%; }
  .band { position: absolute; left: 0; bottom: 0; width: 100%; height: 17px; background: var(--band); }
  .abs { position: absolute; }

  /* front */
  .title {
    font-family: "Poppins", sans-serif;
    font-weight: 600;
    font-size: 45px;
    letter-spacing: 1px;
    line-height: 1;
    color: var(--white);
  }
  .front-title { right: 21px; top: 34px; }
  .front-question {
    right: 21px; top: 101px; width: 330px;
    text-align: right;
    font-family: "Poppins", sans-serif; font-weight: 700;
    font-size: 19px; line-height: 24px; color: var(--teal);
  }
  .front-story {
    right: 21px; top: 157px; width: 310px;
    text-align: right; font-size: 14.6px; line-height: 20.6px;
  }
  .photo {
    left: 0; top: 58px; width: 495px; height: 345px;
    background: linear-gradient(180deg, #3a4654 0%, #2a2f38 45%, #1c2430 100%);
  }
  .heading {
    font-family: "Poppins", sans-serif; font-weight: 700;
    font-size: 19.5px; line-height: 24px; color: var(--ink);
  }
  .body-dark { font-size: 14.6px; line-height: 20.6px; color: var(--ink-soft); }
  .intro { left: 21px; top: 387px; width: 350px; }
  .intro .body-dark { margin-top: 8px; }
  .divider { left: 394px; top: 413px; width: 2px; height: 109px; background: var(--ink); }
  .condition { right: 21px; top: 426px; width: 360px; text-align: right; }
  .condition .body-dark { margin-top: 14px; }

  /* back */
  .back-title { left: 44px; top: 32px; font-size: 39px; }
  .stamp { left: 664px; top: 58px; width: 80px; height: 80px; border: 1px solid #c9d3da; }
  .back-story { left: 41px; top: 92px; width: 560px; font-size: 14.6px; line-height: 20.6px; }
  .mugshot { top: 168px; width: 80px; height: 80px; }
  .mugshot--left { left: 40px; background: linear-gradient(180deg, #f4f4f4 0%, #e4e4e4 70%, #3e4a3c 100%); }
  .mugshot--right { left: 145px; background: linear-gradient(180deg, #f4f4f4 0%, #e4e4e4 70%, #3e4a3c 100%); }
  .mugshot--front { left: 255px; background: linear-gradient(180deg, #ededed 0%, #cfcfcf 60%, #2d332d 100%); }
  .charge {
    top: 255px; width: 90px; text-align: center;
    font-family: "Poppins", sans-serif; font-weight: 600;
    font-size: 12.5px; line-height: 15px;
  }
  .charge--trespass { left: 35px; }
  .charge--mischief { left: 140px; }
  .goal { left: 41px; top: 293px; width: 300px; font-size: 14.6px; line-height: 20.6px; }
  .connector { left: 395px; top: 164px; width: 1px; height: 98px; background: #d8e0e6; }
  .address-line { left: 522px; width: 222px; height: 0; border-top: 1px dashed #9fb2c0; }
  .complaint {
    left: 333px; width: 91px; height: 119px;
    background: var(--paper);
    box-shadow: 0 1px 4px rgba(0,0,0,.35);
    padding: 6px 5px;
    color: #222;
    font-size: 3.6px; line-height: 5px;
  }
  .complaint--one { top: 262px; }
  .complaint--two { top: 394px; }
  .complaint .doc-head { font-weight: bold; margin-bottom: 3px; }
  .complaint .doc-line { height: 1.4px; background: var(--rule); margin: 2.2px 0; }
  .complaint .doc-line.short { width: 55%; margin-left: auto; }
  .complaint .doc-sign { margin: 4px 0 4px 45%; height: 6px; border-bottom: 1px solid #333; }
  .closing { left: 34px; top: 358px; width: 300px; }
  .closing .body-dark { font-size: 13.6px; line-height: 20.6px; }
  .kickbacks { margin-top: 9px; font-size: 19.5px; }
  .hire { margin-top: 3px; }
  .say-no {
    margin-top: 10px;
    font-family: "Poppins", sans-serif; font-weight: 700;
    font-size: 11.6px; line-height: 16.5px; color: var(--ink);
  }
</style>
</head>
<body>

<section class="card card--front">
  <div class="abs photo" role="img" aria-label="Photo of two smiling men in dark suits and white shirts standing side by side"></div>
  <svg class="wave" viewBox="0 0 791 553" preserveAspectRatio="none" aria-hidden="true">
    <path d="M0,344 C120,318 300,370 495,395 C620,410 720,372 791,325 L791,553 L0,553 Z" fill="#ffffff"/>
  </svg>
  <h1 class="abs title front-title">DWIGHT'S REVENGE</h1>
  <h2 class="abs front-question">Why would Dwight Kessler align himself with Gordon Pruett?</h2>
  <p class="abs front-story">Dwight approached elected officials that he wanted to run for office, but did not have money to finance his campaign. He wanted other elected officials to finance his campaign. Everyone told him that they would help him get the vote out, but that he needed to finance his own race.</p>

  <div class="abs intro">
    <h3 class="heading">In comes<br>Gordon Pruett.</h3>
    <p class="body-dark">Gordon Pruett who has a pay to play scheme over at the City, told Dwight he would finance his campaign on one condition.</p>
  </div>
  <div class="abs divider"></div>
  <div class="abs condition">
    <h3 class="heading">He needed to run<br>against Steven Hulse.</h3>
    <p class="body-dark">Why would Dwight want to run with no money?</p>
  </div>
  <div class="band"></div>
</section>

<section class="card card--back">
  <svg class="wave" viewBox="0 0 792 554" preserveAspectRatio="none" aria-hidden="true">
    <path d="M0,339 C150,318 300,352 450,382 C600,412 700,382 792,312 L792,554 L0,554 Z" fill="#ffffff"/>
  </svg>
  <h1 class="abs title back-title">DOMESTIC VIOLENCE</h1>
  <div class="abs stamp"></div>
  <p class="abs back-story">Dwight decided to run because no one on the school board would terminate Dwight's ex and her new boyfriend who both work for the school district. His ex even filed criminal charges against him that are still pending.</p>

  <div class="abs mugshot mugshot--left" role="img" aria-label="Booking photo, profile facing right"></div>
  <div class="abs mugshot mugshot--right" role="img" aria-label="Booking photo, profile facing left"></div>
  <div class="abs mugshot mugshot--front" role="img" aria-label="Booking photo, facing front"></div>
  <p class="abs charge charge--trespass">Criminal<br>TRESPASS</p>
  <p class="abs charge charge--mischief">Criminal<br>MISCHIEF</p>
  <p class="abs goal">Dwight's ultimate goal is to terminate his ex and her new boyfriend if elected.</p>
  <div class="abs connector"></div>

  <div class="abs address-line" style="top:175px"></div>
  <div class="abs address-line" style="top:207px"></div>
  <div class="abs address-line" style="top:239px"></div>
  <div class="abs address-line" style="top:270px"></div>
  <div class="abs address-line" style="top:302px"></div>

  <div class="abs complaint complaint--one">
    <div class="doc-head">THE STATE OF TEXAS<br>COUNTY COMPLAINT NO. 1</div>
    <div class="doc-line"></div><div class="doc-line"></div><div class="doc-line"></div><div class="doc-line"></div>
    <div class="doc-sign"></div>
    <div class="doc-line short"></div>
    <div>Charge: Criminal Trespass</div>
    <div class="doc-line"></div><div class="doc-line"></div><div class="doc-line"></div>
    <div class="doc-sign"></div>
    <div class="doc-line short"></div><div class="doc-line"></div>
  </div>
  <div class="abs complaint complaint--two">
    <div class="doc-head">THE STATE OF TEXAS<br>COUNTY COMPLAINT NO. 2</div>
    <div class="doc-line"></div><div class="doc-line"></div><div class="doc-line"></div><div class="doc-line"></div>
    <div class="doc-sign"></div>
    <div class="doc-line short"></div>
    <div>Charge: Criminal Mischief</div>
    <div class="doc-line"></div><div class="doc-line"></div><div class="doc-line"></div>
    <div class="doc-sign"></div>
    <div class="doc-line short"></div><div class="doc-line"></div>
  </div>

  <div class="abs closing">
    <p class="body-dark">Plus Gordon Pruett needs<br>the majority on the school board to<br>do what he does bet.</p>
    <h3 class="heading kickbacks">Kickbacks for Contracts.</h3>
    <p class="body-dark hire">They will hire their own contractors!</p>
    <p class="say-no">Say "No" to Dwight's Revenge<br>and Gordon Pruett Money Grab!</p>
  </div>
  <div class="band"></div>
</section>

</body>
</html>
```